Varen Psychiatry (Psychiatry clinic offering cutting edge treatments)

2 sided flyer for new psychiatry practice in Boulder, CO. I want something that looks professional, cutting edge, but also welcoming and friendly. My logo and pictures are attached.

Some of the copy:
Personalized, holistic Psychiatry combined with cutting-edge, evidence-based treatments. Our personalized psychiatry plan includes a bio-psycho-social evaluation, personalized treatment plan, medical evaluation for underlying hormonal and electrolyte abnormalities, and genetic testing (when warranted).

We specialize in treatment-resistant depression and substance abuse. We also treat PTSD, Bipolar Disorder, OCD, anxiety disorders, ADHD, and psychotic disorders.

About Dr. Pim- Dr. Pim served as Chief Resident at the largest private psychiatry hospital in Colorado. While there he won 3 consecutive awards for exceptionally high Psychiatry in service test score (99th percentile). He was a board member of Westfield Psychiatric Guild and helped advocate for better Colorado mental health policy. Dr. Pim is uniquely trained in Ketamine, Transcranial Magnetic Stimulation, and integrative psychiatry.

Target Market(s)

Private pay mental health patients, planning to give out to psychologists and family practice doctors

Industry/Entity Type

Medicine/Psychiatry

Colors
0054AA
0677BA
7BADD7
CADEEF
E8F1F8
0094D4
00A9DD
6FCCEA
C7EBF8
E9F6FB
00AB8E
00BBA5
67D7C9
C6EFE9
E9F9F6

Requirements
Must have
• My logo, an about me (Dr. Tom Pim) section

```html
<!DOCTYPE html>
<html lang="en">
<head>
<meta charset="utf-8">
<title>Varen Psychiatry – Two-Sided Flyer</title>
<link rel="stylesheet" href="https://fonts.googleapis.com/css2?family=Poppins:wght@400;500;600;700;800&display=swap">
<style>
  :root{
    --canvas:#dcdce0;
    --paper:#ffffff;
    --navy:#0b0f5e;
    --navy-deep:#070a45;
    --royal:#2433c9;
    --blue:#3b5bf0;
    --cyan:#18c2f0;
    --violet:#8a3cf0;
    --lilac:#d9c8fb;
    --ink:#141414;
    --grey:#8d8d95;
    --band:#3e5cf2;
  }
  *{margin:0;padding:0;box-sizing:border-box}
  html,body{width:685px;height:1200px;overflow:hidden}
  body{background:var(--canvas);font-family:"Poppins",Arial,sans-serif;color:var(--ink);position:relative}
  .page{position:absolute;left:137px;width:410px;height:580px;background:var(--paper);overflow:hidden;box-shadow:0 4px 10px rgba(0,0,0,.25)}
  .page--front{top:13px}
  .page--back{top:607px}
  .abs{position:absolute}
  .placeholder{position:absolute}

  /* front */
  .brand{left:25px;top:30px;display:flex;align-items:center;gap:6px}
  .brand__dot{width:20px;height:20px;border-radius:50%;background:var(--blue)}
  .brand__name{font-weight:700;font-size:13px;color:#5d5d66;line-height:1}
  .headline{left:27px;top:86px;font-weight:700;font-size:13.5px;line-height:15px;text-transform:uppercase}
  .headline .accent{color:var(--blue)}
  .headline .light{font-weight:500}
  .headline .muted{color:var(--grey)}
  .dots{display:flex;gap:2px}
  .dots i{width:3px;height:3px;border-radius:50%;background:var(--violet);display:block}
  .intro{left:27px;top:173px;width:165px;font-size:6px;line-height:7.6px;color:#333}
  .subhead{left:27px;top:222px;font-weight:700;font-size:8.5px;color:var(--violet)}
  .conditions{left:27px;top:239px;list-style:none}
  .conditions li{display:flex;align-items:center;gap:6px;font-size:7px;font-weight:500;height:15.5px}
  .conditions li::before{content:"";width:8px;height:6px;border-radius:50% 50% 40% 40%;background:var(--cyan)}
  .divider{left:199px;top:218px;width:1px;height:66px;background:#cfcfd8}
  .approach{left:207px;top:218px;width:182px;font-size:6px;line-height:7.6px;color:#222}
  .story{left:27px;top:402px;width:166px;font-size:6px;line-height:8px;color:#fff}
  .site{font-weight:600;font-size:11px;letter-spacing:.6px;color:#fff}
  .site b{font-weight:700}
  .site span{color:var(--cyan);font-weight:600}
  .site--front{left:27px;top:543px}

  /* back */
  .plan-kicker{left:26px;top:27px;font-weight:700;font-size:12px;color:var(--cyan);line-height:13px}
  .plan-title{left:26px;top:40px;font-weight:800;font-size:20px;color:#fff;line-height:21px}
  .plan-sub{left:26px;top:61px;font-weight:500;font-size:10px;letter-spacing:3.2px;color:var(--violet);line-height:12px}
  .dots--back{left:26px;top:77px}
  .plan-list{left:26px;top:92px;list-style:none;color:#fff}
  .plan-list li{display:flex;gap:5px;font-size:6.2px;font-weight:600;line-height:7.4px;margin-bottom:5.4px;width:200px}
  .plan-list li::before{content:"";flex:none;width:8px;height:6px;margin-top:1px;border-radius:50% 50% 40% 40%;background:var(--cyan)}
  .plan-text{left:26px;top:163px;width:285px;font-size:5.9px;line-height:7.4px;color:#e8e9ff}
  .pride{left:258px;top:283px;font-weight:700;font-size:9.5px;line-height:12.3px}
  .pride .accent{color:var(--blue)}
  .pride .muted{color:var(--grey)}
  .rule{left:124px;top:377px;width:286px;height:1px;background:var(--violet)}
  .frame{left:28px;top:385px;width:140px;height:157px;border-left:1px solid var(--violet);border-bottom:1px solid var(--violet);border-radius:0 0 0 14px}
  .frame::before{content:"";position:absolute;left:-1px;top:-1px;width:14px;height:14px;border-top:1px solid var(--violet);border-left:1px solid var(--violet);border-radius:14px 0 0 0}
  .frame__dot{left:97px;top:539px;width:6px;height:6px;border-radius:50%;background:var(--violet)}
  .bio{left:47px;top:391px;width:198px;font-size:5.9px;line-height:7.8px;color:#222}
  .bio .role{color:var(--blue);font-weight:700}
  .bio b{font-weight:700}
  .nameband{left:211px;top:529px;width:199px;height:28px;background:var(--band);border-radius:10px 0 0 0;color:#fff;display:flex;align-items:center;gap:5px;padding-left:30px}
  .nameband strong{font-size:12px;font-weight:700}
  .nameband span{font-size:6.5px;font-weight:500;letter-spacing:.3px}
  .site--back{left:27px;top:545px;color:#111}
  .site--back span{color:var(--royal)}
</style>
</head>
<body>

<section class="page page--front">
  <div class="placeholder" role="img" aria-label="Profile of a woman in violet light merging into a blue circuit-line graphic"
       style="left:176px;top:0;width:234px;height:225px;border-radius:0 0 0 110px;background:linear-gradient(135deg,#e6dafc 0%,#b79af5 22%,#7c5cf5 45%,#4f4ce8 65%,#3b5bf0 80%,#8fb6fb 100%)"></div>

  <div class="abs brand"><span class="brand__dot"></span><span class="brand__name">Varen Psychiatry</span></div>

  <h1 class="abs headline">
    <span class="accent">Varen Psychiatry</span><br>
    <span class="light">Is</span> Now Accepting<br>
    New Patients <span class="light">in</span><br>
    <span class="muted">Boulder,</span><br>
    <span class="muted">Colorado!</span>
  </h1>
  <div class="abs dots" style="left:27px;top:163px"><i></i><i></i><i></i><i></i></div>

  <p class="abs intro">We specialize in treating patients with treatment resistant depression and substance abuse disorders who have not responded to other forms of treatment.</p>

  <h2 class="abs subhead">WE ALSO TREAT PATIENTS WITH</h2>
  <ul class="abs conditions">
    <li>PTSD</li><li>Bipolar Disorder</li><li>OCD</li><li>Anxiety disorders</li><li>ADHD</li><li>Psychotic disorders</li>
  </ul>

  <div class="abs divider"></div>
  <p class="abs approach">We know that mental health is complex and that multiple factors can contribute to the development of mental illness. For this reason, we take an integrative approach that considers the whole person. We understand that each individual has their own unique set of experiences, strengths, and challenges, and we tailor our treatment plans to suit each patient’s personal needs.</p>

  <svg class="abs" style="left:0;top:300px" width="410" height="280" viewBox="0 0 410 280" aria-hidden="true">
    <defs><linearGradient id="navyFront" x1="0" y1="0" x2="1" y2="1"><stop offset="0" stop-color="#0b0f5e"/><stop offset="1" stop-color="#14207a"/></linearGradient></defs>
    <path d="M0 90 C90 40 200 30 300 18 C340 14 380 14 410 16 L410 280 L0 280 Z" fill="url(#navyFront)"/>
  </svg>
  <div class="placeholder" role="img" aria-label="Glowing blue brain hovering above a futuristic pedestal"
       style="left:204px;top:318px;width:200px;height:248px;border-radius:12px;background:linear-gradient(180deg,#1c2690 0%,#2f4fd6 30%,#4a8cf5 50%,#2a47c9 72%,#3d6ef0 88%,#1a2486 100%)"></div>

  <p class="abs story">So often, when we think about mental health, we focus on just treating symptoms. If someone is depressed, they might take medication to help them feel better. If someone is anxious, they might see a therapist to help them manage their anxiety. While these treatments can be helpful, they only address the symptoms of mental illness. To truly address mental health, it is necessary to treat the root causes. This might involve addressing childhood trauma, unresolved conflict, or feelings of worthlessness. It might also involve developing healthy coping mechanisms and learning how to set boundaries. By treating the root causes of mental illness, we can begin to create lasting change.</p>

  <p class="abs site site--front">www.<b>varenpsych</b><span>.com</span></p>
</section>

<section class="page page--back">
  <div class="placeholder" role="img" aria-label="Therapy session: a woman taking notes while a young man sits with his face in his hands"
       style="left:0;top:200px;width:255px;height:177px;background:linear-gradient(90deg,#d6d9e2 0%,#c4c9d6 40%,#dfe2ea 75%,#f4f5f8 100%)"></div>

  <svg class="abs" style="left:0;top:0" width="410" height="280" viewBox="0 0 410 280" aria-hidden="true">
    <defs><linearGradient id="navyBack" x1="0" y1="0" x2="1" y2="1"><stop offset="0" stop-color="#14188a"/><stop offset="1" stop-color="#0b0f5e"/></linearGradient></defs>
    <path d="M0 0 H410 V272 C370 270 340 250 300 232 C260 214 235 236 200 240 C140 246 80 208 0 208 Z" fill="url(#navyBack)"/>
  </svg>
  <div class="placeholder" role="img" aria-label="Profile of a bearded man with a glowing blue network graphic over his head"
       style="left:262px;top:0;width:148px;height:262px;border-radius:0 0 0 40px;background:linear-gradient(160deg,#3d6ef0 0%,#2a3fc0 30%,#1f2aa0 60%,#141a78 100%)"></div>

  <p class="abs plan-kicker">OUR PERSONALIZED</p>
  <h2 class="abs plan-title">PSYCHIATRY</h2>
  <p class="abs plan-sub">PLAN INCLUDES</p>
  <div class="abs dots dots--back"><i></i><i></i><i></i><i></i></div>

  <ul class="abs plan-list">
    <li>Plan includes a bio-psycho-social evaluation,</li>
    <li>Tailored treatment plan</li>
    <li>Medical evaluation for underlying hormonal and Electrolyte abnormalities</li>
    <li>Genetic testing (when warranted)</li>
  </ul>
  <p class="abs plan-text">Our integrative psychiatry approach combines cutting edge, evidence-based treatments with holistic therapies to provide you with the best possible care. In addition, we also offer Ketamine Assisted Therapy, TMS (Transcranial Magnetic Simulation), and MAT Treatment for Substance abuse.</p>

  <p class="abs pride"><span class="accent">We pride ourselves</span><br>on always<br>staying up to date on<br><span class="muted">the latest mental<br>health treatments</span></p>

  <div class="abs rule"></div>
  <div class="placeholder" role="img" aria-label="Portrait of a smiling psychiatrist in a lavender shirt"
       style="left:245px;top:378px;width:165px;height:202px;background:linear-gradient(180deg,#ece4f8 0%,#dccff4 35%,#c9b8ef 70%,#b9a4ea 100%)"></div>
  <div class="abs frame"></div>
  <div class="abs frame__dot"></div>

  <p class="abs bio"><b>Dr. Tom Pim</b> is a <span class="role">psychiatrist</span> with years of experience providing compassionate, evidence-based care to patients of all ages. He is uniquely trained in several cutting-edge treatments, including Ketamine, Transcranial Magnetic Stimulation (TMS), and integrative psychiatry. Prior to founding Varen Psychiatry, Dr. Pim served as Chief Resident at the largest private psychiatry hospital in Colorado. While there, he won three consecutive awards for exceptionally high Psychiatry in-service test scores (99th percentile). In addition, he was a board member of the Westfield Psychiatric Guild and helped advocate for better Colorado mental health policy. Thanks to his extensive training and experience, Dr. Pim is able to provide each patient with an individualized treatment plan that brings optimum results.</p>

  <div class="abs nameband"><strong>Dr. Tom Pim</strong><span>PSYCHIATRIST</span></div>
  <p class="abs site site--back">www.<span>varenpsych</span>.com</p>
</section>

</body>
</html>
```